A website for Veltranor Limited

We need a new and modern website for our company. We are engineering consultants and contractors (EPC) in the oil and gas industry and building services industry.
What we do:
Engineering, procurement, construction
Automation (safety and process)
Non-destructive testing
Training
We have an existing website and the content can be referred from there since we are remaking the website
For more information visit Veltranor Limited Kenya

```html
<!DOCTYPE html>
<html lang="en">
<head>
<meta charset="utf-8">
<title>Veltranor Limited</title>
<link href="https://fonts.googleapis.com/css2?family=Poppins:wght@300;400;500;600;700&display=swap" rel="stylesheet">
<style>
:root{
  --brand:#a53a22;
  --accent:#e8613b;
  --orange:#f4b566;
  --ink:#2b2b2b;
  --text:#444;
  --soft:#f4f4f4;
  --footer:#3a3a3a;
}
*{box-sizing:border-box;margin:0;padding:0}
html,body{width:1200px;height:3871px;overflow:hidden}
body{font-family:'Poppins',sans-serif;color:var(--text);background:#fff;position:relative}
.abs{position:absolute}
.header{top:0;left:0;width:1200px;height:135px;background:#fff}
.logo{left:75px;top:25px;display:flex;align-items:center;gap:4px}
.logo-mark{width:80px;height:80px;border:3px solid var(--brand);border-radius:50%;display:flex;align-items:center;justify-content:center}
.logo-mark span{width:50px;height:50px;background:var(--accent);border-radius:50%}
.logo-name{font-weight:300;color:var(--brand);font-size:24px;line-height:32px;letter-spacing:1px}
.call{left:698px;top:40px;display:flex;gap:14px;align-items:center}
.call-icon{width:58px;height:58px;border:2px solid var(--brand);border-radius:50%;display:flex;align-items:center;justify-content:center}
.call-label{color:var(--brand);font-weight:600;font-size:19px}
.call-nums{color:var(--ink);font-size:20px}
.nav{top:135px;left:0;width:1200px;height:57px;background:var(--brand);display:flex;align-items:center;padding-left:83px;gap:25px}
.nav a{color:#fff;font-weight:600;font-size:14px;text-decoration:none;letter-spacing:.2px}
.hero{top:192px;left:0;width:1200px;height:620px;background:linear-gradient(160deg,#5a5a5e 0%,#7a5a48 40%,#9a6a4a 55%,#4a4c52 100%)}
.hero-title{top:368px;left:0;width:1200px;text-align:center;color:#fff;font-weight:700;font-size:78px;letter-spacing:1px}
.hero-sub{top:462px;left:0;width:1200px;text-align:center;color:#fff;font-size:26px;line-height:35px}
.btn{background:var(--accent);color:#fff;font-weight:600;font-size:16px;text-align:center;border-radius:2px}
.hero-btn{top:560px;left:512px;width:178px;height:54px;line-height:54px}
.dots{top:759px;left:554px;display:flex;gap:14px}
.dots i{width:13px;height:13px;border-radius:50%;background:#fff}
.dots i:first-child{background:var(--accent)}
.about-photo{left:137px;top:967px;width:450px;height:366px;background:linear-gradient(180deg,#8fb3d6,#b8b0a0 55%,#6a6a5a)}
.about-title{left:615px;top:972px;font-weight:600;font-size:38px;color:var(--ink)}
.about-text{left:615px;top:1030px;width:500px;font-size:15.5px;line-height:27.5px;color:var(--ink)}
.about-text p{margin-bottom:10px}
.about-btn{left:615px;top:1259px;width:179px;height:54px;line-height:54px}
.services{top:1482px;left:0;width:1200px;height:642px;background:var(--orange)}
.sec-title{left:0;width:1200px;text-align:center;font-weight:600;font-size:38px;color:var(--ink)}
.services .sec-title{color:#fff;top:80px}
.card{top:165px;width:328px;height:383px;color:#fff}
.card-label{position:absolute;left:24px;bottom:20px;font-size:28px;line-height:34px;letter-spacing:.5px}
.tabs{top:2274px;left:206px;display:flex;align-items:center;gap:32px;font-size:17px;color:var(--ink)}
.tab-active{background:var(--accent);color:#fff;padding:8px 16px}
.tile{width:338px;height:263px}
.proj-btn{left:495px;top:2966px;width:210px;height:51px;line-height:51px}
.clients{top:3101px;left:0;width:1200px;height:285px;background:var(--soft)}
.client-row{top:137px;left:75px;width:1050px;display:flex;justify-content:space-between;align-items:center}
.client-row span{font-size:34px;font-weight:500;color:#9a9ea6}
.contact-col{top:3520px;font-size:17px;line-height:31px;color:var(--ink)}
.contact-col h4{color:var(--accent);font-weight:600;font-size:17px;margin-bottom:4px}
.contact-col p{margin-bottom:6px}
.footer{top:3807px;left:0;width:1200px;height:64px;background:var(--footer);color:#fff}
.copy{left:75px;top:23px;font-size:13px}
.social{right:75px;top:22px;display:flex;gap:22px}
.social i{width:22px;height:22px;background:#9a9a9a;border-radius:3px}
</style>
</head>
<body>
<header class="abs header">
  <div class="abs logo">
    <div class="logo-mark"><span></span></div>
    <div class="logo-name">VELTRANOR<br>LIMITED</div>
  </div>
  <div class="abs call">
    <div class="call-icon"><svg width="26" height="26" viewBox="0 0 24 24"><path d="M6.6 10.8a15 15 0 006.6 6.6l2.2-2.2c.3-.3.7-.4 1-.2 1.1.4 2.3.6 3.6.6.6 0 1 .4 1 1V20c0 .6-.4 1-1 1A17 17 0 013 4c0-.6.4-1 1-1h3.5c.6 0 1 .4 1 1 0 1.3.2 2.5.6 3.6.1.3 0 .7-.2 1z" fill="var(--brand)"/></svg></div>
    <div><div class="call-label">CALL US:</div><div class="call-nums">+254 700 410 552, +254 700 410 553</div></div>
  </div>
</header>
<nav class="abs nav">
  <a>HOME</a><a>ABOUT US</a><a>SERVICES</a><a>PRODUCTS</a><a>OUR PROJECTS</a><a>OUR CLIENTS</a><a>WHERE WE OPERATE</a><a>OUR PARTNERS</a><a>CONTACT</a>
</nav>
<section class="abs hero" role="img" aria-label="Industrial plant with pipes and valves"></section>
<h1 class="abs hero-title">VELTRANOR LIMITED</h1>
<p class="abs hero-sub">Design, Supply, Installation and Commissioning of<br>LPG and Petroleum systems</p>
<div class="abs btn hero-btn">READ MORE</div>
<div class="abs dots"><i></i><i></i><i></i><i></i></div>

<svg class="abs" style="left:20px;top:890px" width="520" height="520" viewBox="0 0 520 520"><path d="M455 68A256 256 0 1 0 455 450" fill="none" stroke="var(--brand)" stroke-width="2.5"/></svg>
<div class="abs about-photo" role="img" aria-label="Two engineers walking on a plant walkway"></div>
<h2 class="abs about-title">ABOUT VELTRANOR LIMITED</h2>
<div class="abs about-text">
  <p>Veltranor undertakes Design, Supply, Installation and Commissioning of LPG and Petroleum systems including LPG Reticulated Systems (piped gas). We also do LPG tank revalidation and recertification.</p>
  <p>Our clients include: Oil companies (both multinationals and local), government agencies, manufacturing companies, agricultural institutions, and the building services industry.</p>
</div>
<div class="abs btn about-btn">READ MORE</div>

<section class="abs services">
  <h2 class="abs sec-title">WHAT WE DO</h2>
  <svg class="abs" style="left:30px;top:328px" width="30" height="52"><path d="M26 2L4 26l22 24" fill="none" stroke="#fff" stroke-width="4"/></svg>
  <svg class="abs" style="left:1140px;top:328px" width="30" height="52"><path d="M4 2l22 24L4 50" fill="none" stroke="#fff" stroke-width="4"/></svg>
  <div class="abs card" style="left:75px;background:linear-gradient(180deg,#6a8fb5,#3e5060 60%,#1e2024)" role="img" aria-label="Engineers in hard hats at a refinery"><div class="card-label">Engineering<br>Procurement<br>Construction</div></div>
  <div class="abs card" style="left:436px;background:linear-gradient(180deg,#7fa0c4,#5a6a7a 50%,#1e2024)" role="img" aria-label="Industrial robot arm in a factory"><div class="card-label">Automation<br>(safety &amp; process)</div></div>
  <div class="abs card" style="left:799px;background:linear-gradient(180deg,#6a5a50,#7a5a40 50%,#1e2024)" role="img" aria-label="Technician inspecting a steel pipe"><div class="card-label">Non-Destructive<br>Testing</div></div>
</section>

<h2 class="abs sec-title" style="top:2190px">PROJECTS</h2>
<div class="abs tabs"><span class="tab-active">Piped Gas – LPG Installation</span><span>Petroleum &amp; LPG Terminals / Depots</span><span style="margin-left:16px">Petrol Stations</span></div>
<div class="abs tile" style="left:74px;top:2367px;background:linear-gradient(180deg,#3a78c0,#e8ecef 55%,#8a7a60)" role="img" aria-label="LPG storage spheres"></div>
<div class="abs tile" style="left:432px;top:2367px;background:linear-gradient(180deg,#3f7fc8,#b8c8d8 50%,#606a74)" role="img" aria-label="Refinery under blue sky"></div>
<div class="abs tile" style="left:788px;top:2367px;background:linear-gradient(180deg,#8a8a86,#6a7060 60%,#4a5a3a)" role="img" aria-label="Inspector checking a gas pipeline"></div>
<div class="abs tile" style="left:74px;top:2650px;background:linear-gradient(180deg,#2a2a2a,#8a6a30 60%,#c89028)" role="img" aria-label="Yellow pipeline in a tunnel"></div>
<div class="abs tile" style="left:432px;top:2650px;background:linear-gradient(180deg,#4a3a20,#c8981e 50%,#2a2a2e)" role="img" aria-label="Engineer with tablet beside yellow pipes"></div>
<div class="abs tile" style="left:788px;top:2650px;background:linear-gradient(180deg,#3a3a3a,#c05a40 50%,#8ac8d0)" role="img" aria-label="Hands fitting a gas regulator"></div>
<div class="abs btn proj-btn">VIEW ALL PROJECTS</div>

<section class="abs clients">
  <h2 class="abs sec-title" style="top:50px">OUR CLIENTS</h2>
  <div class="abs client-row"><span>Brightmere</span><span>Northwell</span><span>Corvana</span><span>Halden &amp; Rowe</span></div>
</section>

<h2 class="abs sec-title" style="top:3430px">CONTACT US</h2>
<div class="abs contact-col" style="left:75px">
  <h4>HEAD OFFICE</h4>
  <p>Kestrel Court,<br>Next to Orion Plaza, Sabaki,<br>Suite 14, Meridian Road<br>P.O. Box 40210-00500 Nairobi</p>
  <p>+254 700 410 560, +254 700 410 552</p>
  <p>info@veltranor.example</p>
</div>
<div class="abs contact-col" style="left:456px">
  <h4>SHOP</h4>
  <p>Harbourline Building, Coastline<br>road Industrial Area<br>P.O. Box 40210-00500 Nairobi</p>
  <p>+254 700 410 560, +254 700 410 552</p>
  <p>info@gasline.example</p>
</div>
<div class="abs contact-col" style="left:844px">
  <h4>RWANDA OFFICE</h4>
  <p>Veltranor Rwanda<br>Plot number 2207, Hillview,<br>Eastside, Kigali.</p>
  <p>+254 700 410 560, +254 700 410 552</p>
  <p>rwanda@veltranor.example</p>
</div>

<footer class="abs footer">
  <div class="abs copy">Copyright © 2023 VELTRANOR. All rights reserved.</div>
  <div class="abs social"><i></i><i></i><i></i><i></i></div>
</footer>
</body>
</html>
```